seeking a modern Business Card design for Roof Plumbering Business

wexcombe roof plumbing is a local metal re-roof and new construction specialist. We are seeking a modern business card to assist with networking within the industry. Our services are predominantly the installation of metal roofs on new houses, however we also do re-roofs when an existing roof needs replacing. We service both residential and commercial properties. Please include the below details on the card:
Name: Owen Wexcombe
Phone: 0471 385 962
Email: owenwexcomberoofing@mailnest.example

Residential & Commercial
Re-roof & New Construction
Fully Insured

I have uploaded our business logo, which we think would suit a black background. Please use all lower case for business name.
Cheers
Updates

Hey Guys, As requested I've uploaded a Pdf version of my logo. Hopefully this help. Thanks

Industry/Entity Type

Business

Contact Information for Business Card

Name: Owen Wexcombe
Phone: 0471 385 962

Residential & Commercial
Fully Insured

Font styles to use
Serif
Sans Serif

Requirements
Must have
• Name must be all lower case "wexcombe roof plumbing"
Nice to have
• Stick with Logo Colours

```html
<!DOCTYPE html>
<html lang="en">
<head>
<meta charset="utf-8">
<title>wexcombe roof plumbing – business card</title>
<link href="https://fonts.googleapis.com/css2?family=Crimson+Text:wght@400;600;700&display=swap" rel="stylesheet">
<style>
  :root {
    --bg: #2b2b2d;
    --card: #f4f4f4;
    --card-edge: #e2e2e2;
    --brand-blue: #1f97c6;
    --slate: #5a5b5e;
    --slate-dark: #4c4d50;
    --ink-grey: #5f5f62;
    --contact-text: #f1f1f1;
    --icon-tile: #d9dadc;
    --icon-glyph: #54565a;
  }
  * { margin: 0; padding: 0; box-sizing: border-box; }
  html, body {
    width: 1200px; height: 997px; overflow: hidden;
    background: var(--bg);
  }
  .canvas {
    position: relative; width: 1200px; height: 997px;
    display: flex; align-items: center; justify-content: center;
  }
  .business-card {
    position: relative; width: 840px; height: 480px;
    border-radius: 26px; overflow: hidden;
    background: linear-gradient(160deg, #ffffff 0%, var(--card) 55%, var(--card-edge) 100%);
    font-family: "Crimson Text", Georgia, serif;
    box-shadow: 0 18px 40px rgba(0,0,0,.45);
  }
  .card-waves { position: absolute; inset: 0; width: 100%; height: 100%; }
  .holder { position: absolute; left: 52px; top: 160px; }
  .holder-name { color: var(--brand-blue); font-size: 32px; font-weight: 700; line-height: 1; }
  .holder-role { color: var(--ink-grey); font-size: 17px; font-weight: 600; margin-top: 4px; }
  .brand { position: absolute; right: 44px; top: 38px; text-align: right; }
  .brand-name {
    display: flex; align-items: center; justify-content: flex-end; gap: 10px;
    color: var(--brand-blue); font-size: 30px; font-weight: 700; line-height: 1;
  }
  .brand-square { width: 16px; height: 16px; background: var(--brand-blue); border-radius: 2px; }
  .services { list-style: none; margin-top: 12px; }
  .services li {
    color: var(--brand-blue); font-size: 16px; font-weight: 700; line-height: 1.55;
  }
  .services li::after { content: " •"; font-size: 11px; vertical-align: 2px; }
  .contact-list {
    position: absolute; left: 40px; bottom: 26px; list-style: none;
  }
  .contact-list li {
    display: flex; align-items: center; gap: 16px;
    color: var(--contact-text); font-size: 23px; letter-spacing: .5px;
    height: 44px;
  }
  .contact-icon {
    width: 30px; height: 30px; border-radius: 6px; background: var(--icon-tile);
    display: flex; align-items: center; justify-content: center; flex: none;
  }
  .contact-icon svg { width: 18px; height: 18px; fill: var(--icon-glyph); }
</style>
</head>
<body>
<main class="canvas">
  <article class="business-card">
    <svg class="card-waves" viewBox="0 0 840 480" preserveAspectRatio="none" aria-hidden="true">
      <path d="M0,330 Q360,228 840,238 L840,480 L0,480 Z" fill="var(--slate)"/>
      <path d="M0,298 Q320,196 660,212 Q340,214 0,322 Z" fill="var(--brand-blue)"/>
    </svg>

    <div class="brand">
      <div class="brand-name"><span class="brand-square"></span>wexcombe roof plumbing</div>
      <ul class="services">
        <li>Fully Insured</li>
        <li>Residential &amp; Commercial</li>
        <li>Re-roof &amp; New Construction</li>
      </ul>
    </div>

    <div class="holder">
      <h1 class="holder-name">Owen Wexcombe</h1>
      <p class="holder-role">Owner</p>
    </div>

    <ul class="contact-list">
      <li>
        <span class="contact-icon"><svg viewBox="0 0 24 24"><path d="M6.6 10.8a15.1 15.1 0 0 0 6.6 6.6l2.2-2.2a1 1 0 0 1 1-.25 11.4 11.4 0 0 0 3.6.57 1 1 0 0 1 1 1V20a1 1 0 0 1-1 1A17 17 0 0 1 3 4a1 1 0 0 1 1-1h3.5a1 1 0 0 1 1 1c0 1.25.2 2.45.57 3.6a1 1 0 0 1-.25 1z"/></svg></span>
        0471 385 962
      </li>
      <li>
        <span class="contact-icon"><svg viewBox="0 0 24 24"><path d="M3 5h18a1 1 0 0 1 1 1v12a1 1 0 0 1-1 1H3a1 1 0 0 1-1-1V6a1 1 0 0 1 1-1zm1 2.2V17h16V7.2l-8 5.3z M4.8 7 12 11.7 19.2 7z"/></svg></span>
        owenwexcomberoofing@mailnest.example
      </li>
      <li>
        <span class="contact-icon"><svg viewBox="0 0 24 24"><path d="M12 2a7 7 0 0 0-7 7c0 5.2 7 13 7 13s7-7.8 7-13a7 7 0 0 0-7-7zm0 9.5A2.5 2.5 0 1 1 12 6.5a2.5 2.5 0 0 1 0 5z"/></svg></span>
        14-16 Harbour Row, Millbrook, Canada.
      </li>
    </ul>
  </article>
</main>
</body>
</html>
```